Redesign of Stillwater Grove website

- I would like to redesign my ministry website (vostel.org)
- Re-brand it with my new logo.

I am looking for something professional and artistic, and focused on creating a good user experience.

The purpose of the site is to:
- Expose VOSTEL to the world
- Inform the public about what we are all about.
- Promote my publications (https://www.bookshelfexample.test/Quiet-Pilgrim-Leaving-Patterned-Paths-ebook/dp/Q7ZX42KT9W/ref=dp_kinw_strp_1)

I don't have to many media material, so I am open to suggestions if the provided images will enhance the look and feel of the site.

Target Market(s)

All English speaking christians , and aspiring Christians around the world.

Industry/Entity Type

Religious

Number of Pages Required

3 page

Font styles to use
Sans Serif

Requirements
Must have
• - Add donation link through CoinBridge
• - A mission page that contains the description found on the "About us" page on Vostel.org
• - A personal author page that will include my bio, publication, and contact information. People should be able to email me right from the page
• - Social media links
Nice to have
• - An address book, were people can send us their contact information.

```html
<!DOCTYPE html>
<html lang="en">
<head>
<meta charset="utf-8">
<title>VOSTEL – A Voice to All Nations</title>
<link href="https://fonts.googleapis.com/css2?family=Oswald:wght@500&family=Roboto:wght@400;500&family=Open+Sans:wght@400;600&display=swap" rel="stylesheet">
<style>
:root{
  --orange:#f5a623;
  --orange-deep:#ec9a12;
  --navy:#0c3561;
  --navy-dark:#082a4f;
  --ink:#333;
  --muted:#666;
  --soft:#f3f3f3;
  --line:#ddd;
  --white:#fff;
}
*{box-sizing:border-box;margin:0;padding:0}
html,body{width:1200px;height:3082px;overflow:hidden}
body{position:relative;font-family:"Open Sans",Arial,sans-serif;color:var(--ink);background:var(--white)}
.abs{position:absolute}
.btn{position:absolute;background:var(--orange);color:var(--white);font:500 13px "Roboto",sans-serif;text-transform:uppercase;display:flex;align-items:center;justify-content:center;border-radius:3px;letter-spacing:.3px}

/* header */
.site-header{position:absolute;left:0;top:0;width:1200px;height:118px;background:var(--white)}
.brand{position:absolute;left:98px;top:20px;display:flex;flex-direction:column}
.brand-name{font:500 46px/1 "Roboto",sans-serif;color:var(--navy);display:flex;align-items:center;gap:8px}
.brand-name .dot{width:12px;height:12px;border-radius:50%;background:var(--orange)}
.brand-tag{font:400 13px "Roboto",sans-serif;color:var(--orange);margin-top:4px;margin-left:2px}
.top-contact{position:absolute;top:24px;font:400 14px "Roboto",sans-serif;color:var(--ink);display:flex;align-items:center;gap:10px}
.top-contact .ic{width:24px;height:24px;border-radius:50%;background:var(--orange);display:flex;align-items:center;justify-content:center}
.main-nav{position:absolute;left:444px;top:78px;display:flex;gap:37px;font:500 13px "Roboto",sans-serif;color:var(--ink)}
.main-nav .active{color:var(--navy);position:relative}
.main-nav .active::after{content:"";position:absolute;left:0;right:0;top:31px;height:3px;background:var(--navy)}

/* hero */
.hero{position:absolute;left:0;top:118px;width:1200px;height:542px;background:linear-gradient(180deg,#6f7b86 0%,#b7a48a 40%,#e69a3c 65%,#3a2416 100%)}
.hero-title{position:absolute;left:98px;top:148px;font:500 44px/1.08 "Oswald",sans-serif;color:var(--white);text-transform:uppercase}
.hero-text{position:absolute;left:98px;top:252px;width:380px;font-size:13px;line-height:1.6;color:#f3ece2}
.hero .btn{left:98px;top:307px;width:118px;height:34px}
.dots{position:absolute;left:98px;top:364px;display:flex;gap:7px}
.dots span{width:13px;height:13px;border-radius:50%;border:2px solid var(--white)}
.dots span:first-child{background:var(--white)}

/* welcome */
.welcome h2{position:absolute;left:115px;top:725px;font:400 34px "Roboto",sans-serif;color:#3c3c3c}
.welcome p{position:absolute;left:115px;width:640px;font-size:11px;line-height:1.95;color:var(--muted)}
.portrait-ring{position:absolute;left:805px;top:728px;width:222px;height:222px;border-radius:50%;border:2px solid #b8c4d6;padding:6px}
.portrait-ring div{width:100%;height:100%;border-radius:50%;background:linear-gradient(160deg,#ece6dc,#c9b8a6 60%,#6d8fb6)}

/* author */
.author{position:absolute;left:0;top:1073px;width:1200px;height:429px;background:linear-gradient(90deg,var(--orange-deep),var(--orange))}
.author-photo{position:absolute;left:0;top:0;width:390px;height:429px;background:linear-gradient(160deg,#f0b440,#7f6a56 50%,#1e2532)}
.author-mark{position:absolute;left:438px;top:58px;width:40px;height:40px;border-radius:50%;background:var(--white)}
.author-name{position:absolute;left:492px;top:52px;font:400 32px "Roboto",sans-serif;color:var(--white)}
.author-sub{position:absolute;left:492px;top:98px;font:400 17px "Roboto",sans-serif;color:var(--white)}
.author p{position:absolute;left:440px;width:580px;font-size:11px;line-height:1.9;color:var(--white)}

/* book */
.book-cover{position:absolute;left:162px;top:1590px;width:220px;height:330px;background:linear-gradient(180deg,#6f6a60,#b5a68a 50%,#4a3f33);box-shadow:8px 8px 0 #3a2e22}
.book h2{position:absolute;left:432px;top:1605px;width:620px;font:500 32px/1.32 "Roboto",sans-serif;color:var(--navy);text-transform:uppercase}
.book p{position:absolute;left:432px;width:600px;font-size:11px;line-height:1.95;color:var(--muted)}
.stars{position:absolute;left:432px;top:1838px;font-size:13px;color:var(--orange);letter-spacing:1px}
.stars span{color:#ccc}
.book .btn{left:432px;top:1865px;width:108px;height:32px}

/* news */
.news{position:absolute;left:0;top:2008px;width:1200px;height:379px;background:var(--soft)}
.news h2{position:absolute;left:96px;top:62px;font:500 24px "Roboto",sans-serif;color:#2c2c2c}
.news-arrows{position:absolute;left:1046px;top:66px;display:flex;gap:6px}
.news-arrows span{width:22px;height:22px;border-radius:50%;border:1px solid #bbb}
.news-item{position:absolute;top:132px}
.news-img{position:absolute;left:0;top:0;width:188px;height:162px}
.news-body{position:absolute;left:214px;top:0;width:290px}
.news-body h3{font:400 17px "Roboto",sans-serif;color:#444}
.news-body .date{font:600 italic 12px "Open Sans",sans-serif;color:var(--orange);margin-top:16px}
.news-body p{font-size:11px;line-height:1.7;color:var(--muted);margin-top:10px}
.news-body .more{font-size:12px;color:#444;margin-top:6px}

/* contact */
.contact h2{position:absolute;left:0;width:1200px;top:2442px;text-align:center;font:400 28px "Roboto",sans-serif;color:#3c3c3c}
.field{position:absolute;top:2516px}
.field label{display:block;font:500 12px "Roboto",sans-serif;color:#444}
.field .input{margin-top:14px;height:38px;border:1px solid var(--line);background:var(--white)}
.contact .btn{left:522px;top:2615px;width:156px;height:38px}

/* footer */
.footer-wave{position:absolute;left:0;top:2690px;width:1200px;height:392px}
.footer-brand{position:absolute;left:98px;top:2750px}
.footer-col{position:absolute;top:2780px;color:var(--white)}
.footer-col h4{font:500 15px "Roboto",sans-serif;text-transform:uppercase;letter-spacing:.3px}
.footer-info{position:absolute;left:98px;top:2866px;color:var(--white);font-size:12px;line-height:1.7}
.footer-info .row{display:flex;gap:14px;align-items:flex-start;margin-top:16px}
.links li{list-style:none;font-size:12px;margin-top:9px;display:flex;gap:16px;align-items:center}
.links li::before{content:"";width:0;height:0;border-left:5px solid var(--white);border-top:4px solid transparent;border-bottom:4px solid transparent}
.news-note{font-size:11px;line-height:1.6;margin-top:18px;width:225px}
.news-input{margin-top:12px;width:225px;height:40px;background:var(--white);color:#777;font-size:10px;padding:14px 10px}
.news-actions{display:flex;gap:12px;margin-top:12px}
.news-actions .sub{width:100px;height:40px;background:var(--orange);font:500 11px "Roboto",sans-serif;display:flex;align-items:center;justify-content:center;text-transform:uppercase}
.news-actions .pay{width:104px;height:40px;background:#f7c14a;border-radius:6px;color:var(--navy);font:600 12px "Open Sans",sans-serif;display:flex;align-items:center;justify-content:center}
.social li{list-style:none;display:flex;gap:10px;align-items:center;font-size:13px;margin-top:13px}
.social li span{width:24px;height:24px;border-radius:50%;border:1.5px solid var(--white)}
.copyright{position:absolute;left:0;width:1200px;top:3040px;text-align:center;font-size:11px;color:var(--white)}
</style>
</head>
<body>

<header class="site-header">
  <div class="brand">
    <div class="brand-name"><span class="dot"></span>VOSTEL</div>
    <div class="brand-tag">A Voice to All Nations</div>
  </div>
  <div class="top-contact" style="left:730px">
    <span class="ic"><svg width="12" height="12" viewBox="0 0 24 24"><path fill="#fff" d="M6.6 10.8a15 15 0 0 0 6.6 6.6l2.2-2.2a1 1 0 0 1 1-.25 11.4 11.4 0 0 0 3.6.6 1 1 0 0 1 1 1V20a1 1 0 0 1-1 1A17 17 0 0 1 3 4a1 1 0 0 1 1-1h3.5a1 1 0 0 1 1 1c0 1.25.2 2.45.6 3.6a1 1 0 0 1-.25 1z"/></svg></span>555.201.4470
  </div>
  <div class="top-contact" style="left:890px">
    <span class="ic"><svg width="12" height="12" viewBox="0 0 24 24"><path fill="#fff" d="M2 5h20v14H2z"/><path d="M2 5l10 8 10-8" stroke="#f5a623" stroke-width="2" fill="none"/></svg></span>elias@vostelmail.org
  </div>
  <nav class="main-nav">
    <span class="active">HOME</span><span>ABOUT US</span><span>MISSION</span><span>AUTHOR</span><span>PUBLICATIONS</span><span>DONATION</span><span>CONTACT US</span>
  </nav>
</header>

<section class="hero" role="img" aria-label="Person with raised arms on a hilltop against a sunset sky">
  <h1 class="hero-title">VOSTEL<br>A Voice to All Nations</h1>
  <p class="hero-text">Sed ut perspiciatis unde omnis iste natus error sit voluptatem accusantium doloremque laudantium, totam</p>
  <div class="btn">Donation&nbsp;<svg width="11" height="11" viewBox="0 0 12 12"><circle cx="6" cy="6" r="5.5" fill="#fff"/><path d="M5 3.5 7.5 6 5 8.5" stroke="#f5a623" stroke-width="1.5" fill="none"/></svg></div>
  <div class="dots"><span></span><span></span><span></span></div>
</section>

<section class="welcome">
  <h2>WELCOME TO VOSTEL</h2>
  <p style="top:780px">Stillwater Grove is a gathering of believers which has for purpose to seek the face of God for an authentic restoration of the church as a body of born again believers around the world. In this age of great scientific innovations and discoveries, the world is undergoing a transformation that only those who can look at it from outside can discern in what direction the change is taking us. Our mindset is being reshaped by the media and new ideas that are inclined toward vices rather than values. A powerful wave that spares no one, no social structure, no traditional ideology or culture.</p>
  <p style="top:895px">As a gathering of believers, Stillwater Grove seeks an awakening of the mind founded on precepts and teachings of Jesus Christ, the ability to discern times and seasons in order for a repositioning of the believer according to Gods plan. We look back and think about where we, the body of Christ, come from, and look into the present to think about where we are, and finally look ahead to think about where we are going.</p>
  <div class="portrait-ring"><div role="img" aria-label="Portrait photo of the ministry couple"></div></div>
</section>

<section class="author">
  <div class="author-photo" role="img" aria-label="Portrait photo of the author seated in a dark suit"></div>
  <div class="author-mark"></div>
  <div class="author-name">ELIAS MARROW</div>
  <div class="author-sub">A Voice to all Nations</div>
  <p style="top:150px">Elias Marrow is a Bible teacher and missionary of the Gospel of Jesus Christ. He is the president and founder of VOSTEL, a missionary organization dedicated to preparing believers for the return of the Lord Jesus Christ. He holds a Bachelor's degree in Computer Science from Northfield State University and has been in ministry for over 15 years. He is married and is a father of 2.</p>
  <p style="top:250px">Elias hopes to show to his generation that:</p>
  <p style="top:285px">Faith and science are not mutually exclusive as many are lead to believe.<br>The most important notion about salvation, is the understanding of what we are being saved from.<br>Therefore repentance from sin should be at the core of our preaching as noted in Luke 24:45-48.<br>The Holy Spirit is still working today as He did back 2000 years ago.</p>
</section>

<section class="book">
  <div class="book-cover" role="img" aria-label="Book cover of The Quiet Pilgrim"></div>
  <h2>The Quiet Pilgrim: Leaving Patterned Paths Digital Edition</h2>
  <p style="top:1700px">Society has changed faster in the past hundred years than in any other period of human history. This change has profound spiritual implications that most of us are completely unaware of. In a unique way, The Quiet Pilgrim exposes a conspiracy that starts from the beginning of time to the end of the world.</p>
  <p style="top:1783px">It tells how Satan has slowly but surely groomed society to become what it is today, and how he has prepared it for the leadership of the Antichrist in the future.</p>
  <div class="stars">★★★<span>☆☆</span></div>
  <div class="btn">Read More</div>
</section>

<section class="news">
  <h2>LATEST NEWS</h2>
  <div class="news-arrows"><span></span><span></span></div>
  <article class="news-item" style="left:98px">
    <div class="news-img" role="img" aria-label="Person with raised arms at sunset" style="background:linear-gradient(180deg,#8aa3bf,#e8a244 60%,#3b2a1a)"></div>
    <div class="news-body">
      <h3>Nulla at diam ornare, aliquam urna</h3>
      <div class="date">MAY 25, 2016</div>
      <p>Nulla at diam ornare, aliquam urna vel, commodo urna. Nam id risus a est luctus consectetur quis eget libero. Suspendisse potenti. Pellentesque habitant morbi tristique senectus</p>
      <div class="more">Read More +</div>
    </div>
  </article>
  <article class="news-item" style="left:630px">
    <div class="news-img" role="img" aria-label="Hands holding a Bible" style="background:linear-gradient(150deg,#2f2c2a,#b78a6a 50%,#7a1f22)"></div>
    <div class="news-body">
      <h3>Nulla at diam ornare, aliquam urna</h3>
      <div class="date">MAY 25, 2016</div>
      <p>Nulla at diam ornare, aliquam urna vel, commodo urna. Nam id risus a est luctus consectetur quis eget libero. Suspendisse potenti. Pellentesque habitant morbi tristique senectus</p>
      <div class="more">Read More +</div>
    </div>
  </article>
</section>

<section class="contact">
  <h2>QUICK CONTACT</h2>
  <div class="field" style="left:135px;width:240px"><label>NAME *</label><div class="input"></div></div>
  <div class="field" style="left:390px;width:215px"><label>EMAIL *</label><div class="input"></div></div>
  <div class="field" style="left:622px;width:215px"><label>PHONE</label><div class="input"></div></div>
  <div class="field" style="left:852px;width:215px"><label>MESSAGE</label><div class="input"></div></div>
  <div class="btn">Send Enquiry</div>
</section>

<footer>
  <svg class="footer-wave" viewBox="0 0 1200 392" preserveAspectRatio="none">
    <path d="M0 30 Q600 -30 1200 30 V392 H0 Z" fill="#0c3561"/>
    <path d="M0 30 Q600 -30 1200 30" stroke="#f5a623" stroke-width="4" fill="none"/>
  </svg>
  <div class="footer-brand brand" style="left:98px;top:2750px">
    <div class="brand-name" style="color:#fff;font-size:42px"><span class="dot"></span>VOSTEL</div>
    <div class="brand-tag">A Voice to All Nations</div>
  </div>
  <div class="footer-info">
    <div>STILLWATER GROVE<br>42 Alder Lane Brookfield, Vermont 05036 USA</div>
    <div class="row"><svg width="16" height="16" viewBox="0 0 24 24"><path fill="none" stroke="#fff" stroke-width="1.6" d="M6.6 10.8a15 15 0 0 0 6.6 6.6l2.2-2.2a1 1 0 0 1 1-.25 11.4 11.4 0 0 0 3.6.6 1 1 0 0 1 1 1V20a1 1 0 0 1-1 1A17 17 0 0 1 3 4a1 1 0 0 1 1-1h3.5a1 1 0 0 1 1 1c0 1.25.2 2.45.6 3.6a1 1 0 0 1-.25 1z"/></svg>Call Us 555.318.2200</div>
    <div class="row"><svg width="16" height="16" viewBox="0 0 24 24"><path fill="none" stroke="#fff" stroke-width="1.6" d="M2 5h20v14H2zM2 5l10 8 10-8"/></svg><span>info@vostelmail.org<br>elias@vostelmail.org</span></div>
  </div>
  <div class="footer-col" style="left:444px">
    <h4>Quick Links</h4>
    <ul class="links" style="margin-top:12px"><li>Home</li><li>About us</li><li>Mission</li><li>Author</li><li>Publications</li><li>Contact us</li></ul>
  </div>
  <div class="footer-col" style="left:663px">
    <h4>Sign up for Newsletter</h4>
    <p class="news-note">Excepteur sint occaecat cupidatat non proident, sunt in culpa qui</p>
    <div class="news-input">Enter Name</div>
    <div class="news-actions"><div class="sub">Subscribe</div><div class="pay">CoinBridge</div></div>
  </div>
  <div class="footer-col" style="left:1002px">
    <h4>Social</h4>
    <ul class="social" style="margin-top:6px">
      <li><span></span>Facenote</li><li><span></span>Chirper</li><li><span></span>Circles+</li><li><span></span>Viewtube</li>
    </ul>
  </div>
  <div class="copyright">2016 © Copyrights Vostel. All Rights Reserved</div>
</footer>

</body>
</html>
```